Football tournament flyer

I would like a quick turn around for this please.
I need a flyer to promote an 11 aside football tournament I am organising to celebrate the 23rd independence of my country Somaliland. Please use the national colours of our flag in the flyer, I have attached a file for your consideration.
The tournament will take place on 10/05/2014, from 9am - 8pm. The venue will be Corrin Open Space, Tavistrel Lane, Enfield, EN7 2QR.
Refreshments, food and entertainment will be provided.
The name of the cup is Warsadle Cup.
Spaces are limited and the entry fee per team is £200. All proceeds are for charity projects in Somaliland.
To register a team contact Faisal Warsame on 07521 804 192 or Bashir Yusuf on 07463 125 870.
The best players will have the opportunity to represent Somaliland in an international game on the 17/05/2014.
The tournament is organised by Dalmar FC and EverKindred Foundation.

```html
<!DOCTYPE html>
<html lang="en">
<head>
<meta charset="utf-8">
<title>Warsadle Cup – Football Tournament Flyer</title>
<link rel="stylesheet" href="https://fonts.googleapis.com/css2?family=Anton&family=Bowlby+One+SC&family=Cinzel:wght@600;700&family=Oswald:wght@500;600&display=swap">
<style>
  :root {
    --red: #e3262b;
    --red-deep: #b5161c;
    --maroon: #6e0d10;
    --green: #1d8a3c;
    --green-deep: #0b4a22;
    --green-dark: #07331a;
    --pitch: #2f8f2a;
    --white: #ffffff;
    --yellow: #f4e23a;
    --navy: #1b2230;
    --steel: #5a5f66;
    --silver: #d6d9dc;
    --ink: #111111;
  }
  * { margin: 0; padding: 0; box-sizing: border-box; }
  html, body { width: 816px; height: 1200px; overflow: hidden; background: var(--white); }
  .flyer { position: relative; width: 816px; height: 1200px; overflow: hidden; background: var(--green-deep); }

  .header-band {
    position: absolute; left: 0; top: 0; width: 816px; height: 156px;
    background: linear-gradient(var(--red), var(--red-deep));
    text-align: center; font-family: "Cinzel", serif; font-weight: 700;
    color: var(--white); letter-spacing: 4px;
  }
  .header-band p { position: absolute; left: 0; width: 100%; font-size: 34px; line-height: 1; }
  .header-band .line-1 { top: 22px; }
  .header-band .line-2 { top: 68px; }
  .header-band .presents { top: 113px; color: var(--maroon); }

  .stadium-scene {
    position: absolute; left: 0; top: 156px; width: 816px; height: 936px;
    background:
      radial-gradient(ellipse at 60% 10%, #3f8f55 0%, transparent 55%),
      linear-gradient(180deg, #0f5a2c 0%, #1f6b34 35%, #2d7c33 55%, var(--pitch) 75%, #3a9a30 100%);
  }

  .flag-art { position: absolute; left: 60px; top: 280px; width: 250px; height: 190px; }
  .trophy-art {
    position: absolute; left: 304px; top: 344px; width: 220px; height: 134px;
    background: linear-gradient(90deg, #8d9296, #eef0f1 45%, #9ea3a7);
    border-radius: 40px 40px 10px 10px;
  }
  .ball-top-art {
    position: absolute; left: 700px; top: 318px; width: 170px; height: 170px; border-radius: 50%;
    background: radial-gradient(circle at 35% 35%, #ffffff, #c9cbcd 60%, #6f7275);
  }
  .price-badge {
    position: absolute; left: 510px; top: 288px; width: 216px; height: 216px; border-radius: 50%;
    background: var(--navy); border: 8px solid var(--silver);
    box-shadow: 0 0 0 3px var(--steel), 0 6px 14px rgba(0,0,0,.5);
    text-align: center; color: var(--white);
  }
  .price-badge .amount { font-family: "Anton", sans-serif; font-size: 86px; line-height: 1; display: block; margin-top: 28px; }
  .price-badge .per-team { font-family: "Oswald", sans-serif; font-weight: 600; font-size: 23px; display: block; margin-top: 4px; }

  .title-panel {
    position: absolute; left: 72px; top: 474px; width: 684px; height: 342px;
    background: #3b3f44; border-radius: 22px; padding: 10px;
    box-shadow: 0 8px 20px rgba(0,0,0,.55);
  }
  .title-panel .bands {
    width: 100%; height: 100%; border-radius: 14px; overflow: hidden;
    background: linear-gradient(180deg, var(--green) 0%, var(--green) 30%, var(--white) 30%, var(--white) 46%, var(--red) 46%);
    position: relative;
  }
  .cup-name {
    position: absolute; left: 0; top: 20px; width: 100%; text-align: center;
    font-family: "Anton", sans-serif; font-size: 132px; line-height: 1; letter-spacing: 1px;
    color: var(--green); -webkit-text-stroke: 4px var(--white);
    text-shadow: 0 5px 0 var(--green-dark), 0 8px 12px rgba(0,0,0,.6);
  }
  .cup-word {
    position: absolute; left: 0; top: 168px; width: 100%; text-align: center;
    font-family: "Anton", sans-serif; font-size: 150px; line-height: 1;
    color: var(--red); -webkit-text-stroke: 4px var(--white);
    text-shadow: 0 5px 0 var(--maroon), 0 8px 12px rgba(0,0,0,.6);
  }
  .event-detail {
    position: absolute; top: 208px; font-family: "Oswald", sans-serif; font-weight: 600;
    font-size: 30px; line-height: 1.25; color: var(--white); text-align: center;
    text-shadow: 0 2px 3px rgba(0,0,0,.5);
  }
  .event-detail.place { left: 8px; width: 200px; }
  .event-detail.when { right: 8px; width: 210px; }
  .event-detail sup { font-size: 18px; }
  .star { color: var(--ink); font-size: 24px; }

  .register-info {
    position: absolute; left: 44px; top: 860px;
    font-family: "Oswald", sans-serif; font-weight: 500; font-size: 26px; line-height: 1.68;
    color: var(--white); text-shadow: 2px 2px 3px var(--ink);
  }
  .venue-info {
    position: absolute; right: 42px; top: 866px; text-align: right; font-style: normal;
    font-family: "Oswald", sans-serif; font-weight: 500; font-size: 25px; line-height: 1.76;
    color: var(--white); text-shadow: 2px 2px 3px var(--ink);
  }
  .venue-info .label { font-size: 38px; font-weight: 600; line-height: 1.2; }

  .ball-bottom-art {
    position: absolute; left: 354px; top: 990px; width: 264px; height: 264px; border-radius: 50%;
    background: radial-gradient(circle at 40% 35%, #ffffff, #cfd1d3 55%, #55585b);
  }

  .footer-band {
    position: absolute; left: 0; top: 1092px; width: 816px; height: 108px;
    background: linear-gradient(var(--green), #137530);
    text-align: center; font-family: "Bowlby One SC", sans-serif; font-size: 22px; line-height: 1.45;
    color: var(--ink); padding-top: 22px;
  }
  .footer-band .highlight { color: var(--yellow); }
</style>
</head>
<body>
<main class="flyer">
  <header class="header-band">
    <p class="line-1">DALMAR FC AND</p>
    <p class="line-2">EVERKINDRED FOUNDATION</p>
    <p class="presents">PRESENTS</p>
  </header>

  <div class="stadium-scene" role="img" aria-label="Floodlit football stadium with crowd stands and a green pitch"></div>

  <svg class="flag-art" viewBox="0 0 250 190" aria-label="Somaliland national flag on a pole" role="img">
    <rect x="6" y="20" width="6" height="170" fill="#d8b24a"/>
    <path d="M12 34 C70 14 120 48 196 24 L196 62 C120 86 70 52 12 72 Z" fill="#1d8a3c"/>
    <path d="M12 72 C70 52 120 86 196 62 L196 100 C120 124 70 90 12 110 Z" fill="#ffffff"/>
    <path d="M12 110 C70 90 120 124 196 100 L196 138 C120 162 70 128 12 148 Z" fill="#e3262b"/>
    <polygon points="50,82 54,94 66,94 56,101 60,113 50,106 40,113 44,101 34,94 46,94" fill="#111"/>
  </svg>

  <div class="trophy-art" role="img" aria-label="Silver football trophies"></div>
  <div class="ball-top-art" role="img" aria-label="Football"></div>

  <div class="price-badge">
    <span class="amount">£200</span>
    <span class="per-team">ENTRY PER TEAM</span>
  </div>

  <section class="title-panel">
    <div class="bands">
      <h1 class="cup-name">WARSADLE</h1>
      <p class="event-detail place">CORRIN OPEN<br><span class="star">★</span> SPACE <span class="star">★</span></p>
      <p class="cup-word">CUP</p>
      <p class="event-detail when">MAY 10<sup>TH</sup> 2014<br><span class="star">★</span> 9AM - 8PM <span class="star">★</span></p>
    </div>
  </section>

  <div class="register-info">
    <p>TO REGISTER A TEAM CONTACT</p>
    <p>FAISAL WARSAME ON 07521 804 192</p>
    <p>BASHIR YUSUF ON 07463 125 870</p>
  </div>

  <address class="venue-info">
    <p class="label">VENUE</p>
    <p>CORRIN OPEN SPACE</p>
    <p>TAVISTREL LANE</p>
    <p>ENFIELD, EN7 2QR</p>
  </address>

  <div class="ball-bottom-art" role="img" aria-label="Football resting on the pitch"></div>

  <footer class="footer-band">
    <p><span class="highlight">THE BEST PLAYERS</span> WILL HAVE THE OPPORTUNITY TO REPRESENT</p>
    <p>SOMALILAND IN AN INTERNATIONAL GAME ON THE <span class="highlight">17/05/2014</span>.</p>
  </footer>
</main>
</body>
</html>
```